Heronfield Wealth Advisors, Inc. Marketing Collateral - 401k Rollover Decisions

We are looking to create a branded one-pager marketing collateral piece talking about 401k Rollovers & the important information people should know. Rough draft of concept & content included below, and we will finalize copy later. Would include a call to action to contact us. Our website and other contact information are available at https://growwithmaplecrest.com/.

Target Market(s)

Working adults ages 55-75 with access to retirement accounts or who have a 401k account. Especially interested in appealing to people who work for small businesses, local businesses, have company stock, and other unique needs in this space.

Industry/Entity Type

Financial services

Font styles to use
Other font styles liked:
• Cambria

Requirements
Must have
• Clear message & call to action
Nice to have
• Highlight how many Americans have been changing jobs since COVID and why it would be worth working with a professional to make decisions on what to do with retirement accounts and assets. (We're working on getting that stat)
Should not have
• Too much text, don't want to inundate with text blocks

```html
<!DOCTYPE html>
<html lang="en">
<head>
<meta charset="utf-8">
<title>Heronfield Wealth Advisors – 401(k) Rollover One-Pager</title>
<link href="https://fonts.googleapis.com/css2?family=Cinzel:wght@400;600&family=Arimo:wght@400;700&display=swap" rel="stylesheet">
<style>
  :root{
    --backdrop:#cfcfd0;
    --paper:#ffffff;
    --ink:#1d1d1d;
    --red:#c4202f;
    --red-deep:#a81c28;
    --black:#111111;
    --foliage-dark:#27302a;
    --foliage-mid:#3b4a3d;
    --pros-tint:#f6ddd8;
    --cons-tint:#dcdde0;
    --white:#ffffff;
  }
  *{box-sizing:border-box;margin:0;padding:0}
  html,body{width:1200px;height:960px;overflow:hidden;background:var(--backdrop)}
  body{font-family:"Arimo",Arial,sans-serif;color:var(--ink)}
  .flyer{position:absolute;left:254px;top:32px;width:692px;height:896px;background:var(--paper);overflow:hidden;box-shadow:0 6px 22px rgba(0,0,0,.18)}

  .brand{position:absolute;left:30px;top:30px;display:flex;align-items:center;gap:8px}
  .brand-mark{width:16px;height:16px;background:var(--red)}
  .brand-name{font-family:"Cinzel",Georgia,serif;font-weight:600;font-size:14px;color:var(--ink);letter-spacing:.5px}

  .hero-foliage{position:absolute;left:0;top:84px;width:300px;height:466px;background:linear-gradient(160deg,var(--foliage-mid),var(--foliage-dark) 70%)}
  .hero-couple{position:absolute;left:300px;top:0;width:392px;height:330px;background:linear-gradient(135deg,#5f7351,#a99e84 55%,#c7b69a)}

  .headline{position:absolute;left:30px;top:160px;font-family:"Cinzel",Georgia,serif;font-size:40px;line-height:1.05;color:var(--white);font-weight:400}
  .headline .accent{color:var(--red)}
  .intro{position:absolute;left:30px;top:330px;width:250px;padding-left:14px;border-left:4px solid var(--red);color:var(--white);font-size:15px;line-height:1.3}

  .option{position:absolute;width:88px;padding-left:8px;border-left:3px solid var(--red);font-size:10px;line-height:1.3}
  .option-title{display:block;color:var(--red);font-weight:700;font-size:12.5px;margin-bottom:3px}
  .option-title .num{margin-right:4px}
  .opt-leave{left:308px;top:470px}
  .opt-roll{left:404px;top:420px}
  .opt-move{left:500px;top:372px}
  .opt-take{left:596px;top:344px;width:88px}

  .fiduciary{position:absolute;left:30px;top:566px;width:296px;font-size:10px;line-height:1.32}

  .rollover{position:absolute;left:344px;top:574px;width:322px}
  .rollover-title{display:flex;align-items:center;gap:8px;color:var(--red);font-weight:700;font-size:15px;margin-bottom:10px}
  .compare{display:grid;grid-template-columns:1fr 1fr;border-top:2px solid var(--black);border-bottom:2px solid var(--red)}
  .compare h3{font-size:12px;text-align:center;padding:5px 0}
  .pros{background:var(--pros-tint)}
  .pros h3{color:var(--red)}
  .cons{background:var(--cons-tint)}
  .compare ul{list-style:none;padding:0 8px 8px;font-size:10px;line-height:1.35}
  .compare li{margin-bottom:6px}

  .hero-friends{position:absolute;left:60px;top:746px;width:240px;height:64px;background:linear-gradient(120deg,#e8e4df,#d9c6b4 60%,#b5764f)}

  .cta{position:absolute;left:0;top:810px;width:220px;height:86px;background:var(--red-deep);display:flex;align-items:center;justify-content:center}
  .cta-text{font-family:"Cinzel",Georgia,serif;color:var(--white);font-size:24px;line-height:1.05;text-align:center}

  .footer-band{position:absolute;left:220px;top:810px;width:472px;height:86px;background:var(--black);display:flex;gap:18px;padding:10px 20px}
  .footer-note{flex:1;color:var(--red);font-size:9.5px;line-height:1.35}
  .contact{width:170px;color:var(--white);font-size:9.5px;line-height:1.4;font-style:normal}
  .contact-phone{font-weight:700;font-size:14px;margin-bottom:4px;display:flex;align-items:center;gap:6px}
</style>
</head>
<body>
<main class="flyer">
  <div class="hero-couple" role="img" aria-label="Photo of a smiling older couple walking together in a garden"></div>
  <div class="hero-foliage" role="img" aria-label="Dark photo of tall green foliage"></div>

  <header class="brand">
    <span class="brand-mark"></span>
    <span class="brand-name">Heronfield Wealth Advisors, Inc.</span>
  </header>

  <h1 class="headline">Know That<br><span class="accent">You Have</span><br>Options</h1>
  <p class="intro">The most important thing to realize when leaving an employer is that you have options for the money that you have worked hard for and saved.</p>

  <div class="option opt-take"><span class="option-title"><span class="num">4</span>Take it</span>There is the option to take the account in cash, but it is not typically advisable due to the tax and potential penalty implications.</div>
  <div class="option opt-move"><span class="option-title"><span class="num">3</span>Move it</span>If you’ve started working at a new company, they will often have their own qualified plan available that you can move your old company’s funds to.</div>
  <div class="option opt-roll"><span class="option-title"><span class="num">2</span>Roll it</span>Depending on the type of qualified plan, you can roll the funds over from the employer plan to an IRA.</div>
  <div class="option opt-leave"><span class="option-title"><span class="num">1</span>Leave it</span>Most employer plans allow you to leave the funds within the qualified plan.</div>

  <p class="fiduciary">It is important to work with a fiduciary to help you evaluate your options and the pros and cons of them. A fiduciary is someone who is obligated to provide you unbiased advice and disclose any conflicts of interest in their recommendations. It can be particularly important to work with a fiduciary if you are retiring early or are generally confused about all of the information and misinformation out there. We recommend working with an expert who has experience with a multitude of different types of qualified plans such as 401(k), 403(b), Employee Stock Ownership Plans, SEP IRAs, etc. Not all plan types are eligible for rollovers, and even if they are, they may vary in the types of plans that they can be rolled in to.</p>

  <section class="rollover">
    <h2 class="rollover-title">Rolling over 401(k) assets to IRA
      <svg width="40" height="22" viewBox="0 0 40 22" aria-hidden="true">
        <circle cx="8" cy="8" r="6" fill="none" stroke="var(--red)" stroke-width="2"/>
        <path d="M5 8h6M8 5v6" stroke="var(--red)" stroke-width="2"/>
        <circle cx="30" cy="8" r="6" fill="none" stroke="var(--black)" stroke-width="2"/>
        <path d="M27 8h6" stroke="var(--black)" stroke-width="2"/>
        <path d="M8 16h22M19 16v5M14 21h10" stroke="var(--black)" stroke-width="2"/>
      </svg>
    </h2>
    <div class="compare">
      <div class="pros">
        <h3>Pros</h3>
        <ul>
          <li>Typically more investment choices in an IRA</li>
          <li>Ability to make contributions to the account even after leaving your former employer</li>
          <li>Choice of investment custodian and investment advisor you work with</li>
        </ul>
      </div>
      <div class="cons">
        <h3>Cons</h3>
        <ul>
          <li>Less protection from creditors</li>
          <li>Less access to funds prior to age 59½</li>
          <li>RMDs on funds at age 72 regardless if you are still working</li>
        </ul>
      </div>
    </div>
  </section>

  <div class="hero-friends" role="img" aria-label="Photo of two older women looking at a phone together"></div>

  <div class="cta"><p class="cta-text">Talk to<br>us if</p></div>

  <footer class="footer-band">
    <p class="footer-note">Every situation is different. Review fees, fund choices, tax rules and timing before you move any savings. A short meeting can help you compare each option side by side and choose a path that fits your goals, your family and your plans for retirement.</p>
    <address class="contact">
      <p class="contact-phone">
        <svg width="12" height="12" viewBox="0 0 24 24" aria-hidden="true"><path fill="var(--white)" d="M6.6 10.8a15.1 15.1 0 0 0 6.6 6.6l2.2-2.2a1 1 0 0 1 1-.25 11.4 11.4 0 0 0 3.6.57 1 1 0 0 1 1 1V20a1 1 0 0 1-1 1A17 17 0 0 1 3 4a1 1 0 0 1 1-1h3.5a1 1 0 0 1 1 1c0 1.25.2 2.450.57 3.57a1 1 0 0 1-.25 1z"/></svg>
        Call Us: 919-555-0187</p>
      <p>Heronfield Wealth Advisors, Inc.</p>
      <p>P.O. Box 4820</p>
      <p>Oakbrook, NC 27599</p>
    </address>
  </footer>
</main>
</body>
</html>
```